BrivoPeak Business Card Design Project

We are looking for a modern, clean business card design for our new company. We are a consulting firm focused on the financial services market providing management and IT consulting to banks, insurance companies, etc. Please include our company logo and company contact information from the attached file in the design. Two versions of the logo are attached, either version is acceptable. Logos are available in other file formats if needed. We would like to include the contact information for both our UK and US offices as well as the following information for each individual card holder: Name, position/title, address, phone number and e-mail address.
Updates
Project Deadline Extended
Reason: A last minute trip over seas has prevented us from finalizing the decision. A decision will be made this week. We apologize for the inconvenience.
Industry/Entity Type
Business
Contact Information for Business Card
Company logo.
Company locations and phone numbers for both the US and UK offices.
Company URL.
Cardholder Name
Cardholder Position/title
Cardholder Address
Cardholder Phone Number
Cardholder e-mail Address
Look and feel
Each slider illustrates characteristics of the customer's brand and the style your logo design should communicate.

```html
<!DOCTYPE html>
<html lang="en">
<head>
<meta charset="UTF-8">
<title>BrivoPeak Partners – Business Card</title>
<link rel="stylesheet" href="https://fonts.googleapis.com/css2?family=Open+Sans:wght@400;600;700&display=swap">
<style>
  :root {
    --navy: #1e3a68;
    --navy-deep: #182f56;
    --navy-text: #2a4777;
    --steel: #6f757d;
    --ink: #4a4f56;
    --paper: #ffffff;
    --backdrop: #e6e8eb;
  }
  * { margin: 0; padding: 0; box-sizing: border-box; }
  html, body { width: 1200px; height: 843px; overflow: hidden; }
  body {
    background: var(--backdrop);
    font-family: "Open Sans", Arial, sans-serif;
    position: relative;
  }
  .card {
    position: absolute;
    top: 267px;
    width: 540px;
    height: 309px;
    border-radius: 4px;
    box-shadow: 0 6px 18px rgba(0,0,0,0.18);
    overflow: hidden;
  }
  /* Back side */
  .card-back { left: 40px; background: var(--navy); }
  .card-back .pattern-field {
    position: absolute; inset: 0;
    background: linear-gradient(135deg, var(--navy) 0%, var(--navy-deep) 100%);
  }
  .card-back .brand-name {
    position: absolute; left: 0; right: 0; top: 132px;
    text-align: center;
    color: var(--paper);
    font-weight: 700; font-size: 30px; letter-spacing: 0.5px;
  }
  .card-back .back-web {
    position: absolute; left: 26px; bottom: 20px;
    color: var(--paper); font-size: 12px; letter-spacing: 0.3px;
  }
  /* Front side */
  .card-front { left: 620px; background: var(--paper); }
  .side-band {
    position: absolute; left: 0; top: 0; bottom: 0; width: 118px;
    background: var(--navy);
  }
  .brand-lockup {
    position: absolute; left: 84px; top: 30px;
    display: flex; align-items: center; gap: 12px;
  }
  .brand-lockup .brand-mark {
    width: 30px; height: 30px; background: var(--steel);
  }
  .brand-lockup .brand-name {
    color: var(--navy-text);
    font-weight: 700; font-size: 29px; letter-spacing: 0.3px;
  }
  .brand-rule {
    position: absolute; left: 200px; top: 80px; width: 300px; height: 2px;
    background: var(--steel);
  }
  .holder {
    position: absolute; left: 142px; top: 104px;
    color: var(--ink); font-size: 12.5px; line-height: 1.45;
  }
  .holder .holder-name {
    color: var(--navy-text); font-weight: 700; font-size: 17px; line-height: 1.2;
  }
  .holder .holder-title { font-size: 12.5px; margin-bottom: 10px; }
  .contact-row { display: flex; align-items: center; gap: 7px; }
  .contact-row svg { width: 11px; height: 11px; flex: none; }
  .office {
    position: absolute; left: 330px; top: 222px;
    color: var(--ink); font-size: 12.5px; line-height: 1.45;
  }
</style>
</head>
<body>

<section class="card card-back" aria-label="Card back">
  <div class="pattern-field" role="img" aria-label="Faint repeated brand pattern on navy"></div>
  <div class="brand-name">BrivoPeak Partners</div>
  <div class="back-web">www.brivopeak.com</div>
</section>

<section class="card card-front" aria-label="Card front">
  <div class="side-band"></div>
  <div class="brand-lockup">
    <span class="brand-mark"></span>
    <span class="brand-name">BrivoPeak Partners</span>
  </div>
  <div class="brand-rule"></div>

  <div class="holder">
    <div class="holder-name">Marcus Hale</div>
    <div class="holder-title">CEO/Founder</div>
    <div>4210 Larkspur Court</div>
    <div>Juneau, Alaska 38217</div>
    <div class="contact-row">
      <svg viewBox="0 0 12 12"><path fill="#1e3a68" d="M2.4 0.6l2 0 0.8 2.6-1.3 1a7 7 0 0 0 2.9 2.9l1-1.3 2.6 0.8 0 2a1 1 0 0 1-1.1 1A9.5 9.5 0 0 1 1.4 1.7a1 1 0 0 1 1-1.1z"/></svg>
      <span>512 780 4416</span>
    </div>
    <div class="contact-row">
      <svg viewBox="0 0 12 12"><rect x="0.6" y="2.2" width="10.8" height="7.6" fill="none" stroke="#1e3a68" stroke-width="1.2"/><path d="M0.8 2.6L6 6.8l5.2-4.2" fill="none" stroke="#1e3a68" stroke-width="1.2"/></svg>
      <span>hello@brivopeak.com</span>
    </div>
    <div class="contact-row">
      <svg viewBox="0 0 12 12"><circle cx="6" cy="6" r="5.2" fill="none" stroke="#1e3a68" stroke-width="1.2"/><ellipse cx="6" cy="6" rx="2.2" ry="5.2" fill="none" stroke="#1e3a68" stroke-width="1"/><path d="M0.8 6h10.4" stroke="#1e3a68" stroke-width="1"/></svg>
      <span>www.brivopeak.com</span>
    </div>
  </div>

  <div class="office">
    <div>4210 Larkspur Court</div>
    <div>Juneau, Alaska 38217</div>
    <div class="contact-row">
      <svg viewBox="0 0 12 12"><path fill="#1e3a68" d="M2.4 0.6l2 0 0.8 2.6-1.3 1a7 7 0 0 0 2.9 2.9l1-1.3 2.6 0.8 0 2a1 1 0 0 1-1.1 1A9.5 9.5 0 0 1 1.4 1.7a1 1 0 0 1 1-1.1z"/></svg>
      <span>512 780 4416</span>
    </div>
  </div>
</section>

</body>
</html>
```